New stationery design project

Until now, Brolin Technology was exclusively geared towards marketing the self-warming toasty-step insole. Corresponding designer material exists for this purpose, which is further used in this line of business. In the meantime, the business purpose has been expanded to include the following activities: "The company provides consulting services and takes on board mandates in the field of energy and information technology as well as personality-enhancing coaching." We now need a suitable stationery design (letterhead, business card) for this new business purpose. The design is intended to convey specialist knowledge and many years of experience

```html
<!DOCTYPE html>
<html lang="en">
<head>
<meta charset="utf-8">
<title>Brolin Technology – Business Card</title>
<link rel="stylesheet" href="https://fonts.googleapis.com/css2?family=Montserrat:wght@600;700&family=Arimo:wght@400&display=swap">
<style>
  :root {
    --stage: #1f1f1f;
    --brand-red: #c62a2a;
    --accent-red: #e81c24;
    --ink: #1d1d1d;
    --ink-soft: #333333;
    --rule: #b5b5b5;
    --paper: #ffffff;
  }
  * { box-sizing: border-box; margin: 0; padding: 0; }
  html, body {
    width: 1200px; height: 1015px; overflow: hidden;
    background: var(--stage);
  }
  .stage {
    position: relative; width: 1200px; height: 1015px;
  }
  .card {
    position: absolute; left: 260px; width: 680px; height: 390px;
    overflow: hidden;
  }
  .card--front { top: 95px; background: var(--brand-red); }
  .card--back  { top: 530px; background: var(--paper); }

  .wordmark {
    font-family: "Montserrat", sans-serif; font-weight: 700;
    display: flex; align-items: center; gap: 12px;
    white-space: nowrap;
  }
  .wordmark__square { width: 18px; height: 18px; flex: none; }

  .card--front .wordmark {
    position: absolute; left: 0; right: 0; top: 160px;
    justify-content: center; color: var(--paper); font-size: 40px;
  }
  .card--front .wordmark__square { background: var(--paper); width: 22px; height: 22px; }
  .card--front .wordmark-rule {
    position: absolute; left: 190px; width: 300px; top: 228px;
    height: 1.5px; background: var(--paper);
  }

  .card--back .wordmark {
    position: absolute; left: 40px; top: 150px;
    color: var(--ink); font-size: 27px;
  }
  .card--back .wordmark__square { background: var(--accent-red); }
  .card--back .wordmark-rule {
    position: absolute; left: 70px; width: 220px; top: 200px;
    height: 1px; background: #777;
  }
  .divider {
    position: absolute; left: 348px; top: 62px; width: 1px; height: 190px;
    background: var(--rule);
  }
  .contact {
    position: absolute; left: 380px; top: 52px;
    font-family: "Arimo", sans-serif; color: var(--ink-soft);
  }
  .contact__name {
    font-family: "Montserrat", sans-serif; font-weight: 700;
    font-size: 23px; color: var(--ink); line-height: 1.1;
  }
  .contact__name span { color: var(--accent-red); }
  .contact__role { font-size: 14px; margin-top: 2px; }
  .contact__list { list-style: none; margin-top: 16px; }
  .contact__list li {
    display: flex; align-items: center; gap: 8px;
    font-size: 14.5px; line-height: 23px;
  }
  .contact__list svg { width: 14px; height: 14px; flex: none; fill: var(--accent-red); }
  .contact__address { font-size: 14.5px; line-height: 21px; margin-top: 14px; }

  .band-dark {
    position: absolute; left: 0; bottom: 0; width: 100%; height: 22px;
    background: var(--ink);
  }
  .band-red {
    position: absolute; right: 0; bottom: 0; width: 285px; height: 84px;
    background: var(--accent-red); border-left: 5px solid var(--paper);
  }
</style>
</head>
<body>
<main class="stage">
  <section class="card card--front" aria-label="Business card front">
    <div class="wordmark"><span class="wordmark__square"></span>Brolin Technology</div>
    <div class="wordmark-rule"></div>
  </section>

  <section class="card card--back" aria-label="Business card back">
    <div class="wordmark"><span class="wordmark__square"></span>Brolin Technology</div>
    <div class="wordmark-rule"></div>
    <div class="divider"></div>
    <div class="contact">
      <p class="contact__name">Martin <span>Keller</span></p>
      <p class="contact__role">Managing Director</p>
      <ul class="contact__list">
        <li><svg viewBox="0 0 24 24" aria-hidden="true"><path d="M6.6 10.8a15.1 15.1 0 0 0 6.6 6.6l2.2-2.2a1 1 0 0 1 1-.25 11.4 11.4 0 0 0 3.6.57 1 1 0 0 1 1 1V20a1 1 0 0 1-1 1A17 17 0 0 1 3 4a1 1 0 0 1 1-1h3.5a1 1 0 0 1 1 1c0 1.25.2 2.45.57 3.6a1 1 0 0 1-.25 1z"/></svg>044-987 654 321</li>
        <li><svg viewBox="0 0 24 24" aria-hidden="true"><path d="M2 5h20v14H2zm2 2v.5l8 5 8-5V7zm0 3v7h16v-7l-8 5z"/></svg>info@brolintech.com</li>
        <li><svg viewBox="0 0 24 24" aria-hidden="true"><path d="M12 2a10 10 0 1 0 0 20 10 10 0 0 0 0-20zm6.9 6h-3a15.7 15.7 0 0 0-1.4-3.6A8 8 0 0 1 18.9 8zM12 4c.8 1.2 1.5 2.5 1.9 4h-3.8c.4-1.5 1.1-2.8 1.9-4zM4.3 14a8.2 8.2 0 0 1 0-4h3.4a16.5 16.5 0 0 0 0 4zm.8 2h3a15.7 15.7 0 0 0 1.4 3.6A8 8 0 0 1 5.1 16zm3-8h-3a8 8 0 0 1 4.4-3.6A15.7 15.7 0 0 0 8.1 8zM12 20c-.8-1.2-1.5-2.5-1.9-4h3.8c-.4 1.5-1.1 2.8-1.9 4zm2.3-6H9.7a14.7 14.7 0 0 1 0-4h4.6a14.7 14.7 0 0 1 0 4zm.2 5.6a15.7 15.7 0 0 0 1.4-3.6h3a8 8 0 0 1-4.4 3.6zm1.8-5.6a16.5 16.5 0 0 0 0-4h3.4a8.2 8.2 0 0 1 0 4z"/></svg>www.brolintech.com</li>
      </ul>
      <p class="contact__address">Lindenweg 12<br>CH - 8000 Talbach</p>
    </div>
    <div class="band-dark"></div>
    <div class="band-red"></div>
  </section>
</main>
</body>
</html>
```